Foot and ankle surgeon requires a website design

I need a website where prospective and established patients can obtain information and then direct them to making appointments. My practice is a highly professional surgical practice specialising in surgery to the foot and ankle. My title is Mr Colin Dwyer, Podiatric Foot & Ankle Surgeon. My qualifications are: BSc MSc FACPS
The practice website will require information on: Locations, phone numbers to make appointments, general background on podiatric surgery,
I would like to include information on: my hospital appointments, surgical fellowships held, training programs undertaken, association memberships, publications written, links to useful websites
A page dedicated to common foot conditions would be useful and also a page with referral information including an online registration section that will be sent direct to the receptionist.
Examples of similar websites include:
http://www.trevorkeplinfeet.com.au/
http://www.vollardfootsurgeon.com.au/
I will provide files on logo, self photos and my personal training history etc.
Also if there is going to be a background theme I personally am associated with surfing and beach activities, it would be great if this was able to be reflected in the design.
Thank you.

```html
<!DOCTYPE html>
<html lang="en">
<head>
<meta charset="utf-8">
<title>Mr Colin Dwyer – Podiatric Foot &amp; Ankle Surgeon</title>
<link href="https://fonts.googleapis.com/css2?family=Open+Sans:wght@400;600;700&display=swap" rel="stylesheet">
<style>
:root{
  --navy:#1a4a7e;
  --blue:#2a8ad6;
  --teal:#2bc4d2;
  --orange:#f26a2e;
  --ink:#333;
  --muted:#888;
  --line:#dcdcdc;
  --panel:#e9e9e9;
  --foot:#f5f5f5;
  --white:#fff;
}
*{box-sizing:border-box;margin:0;padding:0}
html,body{width:1020px;height:1200px;overflow:hidden;background:var(--white)}
body{position:relative;font-family:"Open Sans",Arial,sans-serif;color:var(--ink)}
.abs{position:absolute}

/* header */
.brand{left:127px;top:22px;display:flex;align-items:center;gap:7px;font-size:14px;font-weight:600;color:var(--navy)}
.brand-dot{width:12px;height:12px;border-radius:50%;background:var(--navy)}
.nav{left:327px;top:0;display:flex;height:45px;font-size:11px;text-transform:uppercase;color:#444}
.nav-item{display:flex;align-items:center;padding:0 13px;height:45px;gap:16px}
.nav-item svg{width:7px;height:5px}
.nav-item.active{background:var(--navy);color:var(--white)}

/* hero */
.hero{left:0;top:74px;width:1020px;height:366px;background:linear-gradient(100deg,#8fb6c8 0%,#c6dbe4 35%,#e6eff3 55%,#9bc9d3 75%,#4fa6b5 100%)}
.tag{left:433px;top:145px;width:154px;height:33px;background:#4a4a4a;color:#eee;font-size:12px;display:flex;align-items:center;justify-content:center;letter-spacing:.3px}
.headline{left:118px;top:198px;width:784px;height:41px;background:var(--blue);color:var(--white);font-size:18px;display:flex;align-items:center;justify-content:center}
.built{left:409px;top:259px;width:201px;height:34px;background:var(--teal);color:var(--white);font-size:12.5px;letter-spacing:1.5px;display:flex;align-items:center;justify-content:center}

.booking{left:126px;top:347px;width:767px;height:93px;background:var(--panel)}
.book-label{left:1px;top:14px;width:190px;height:64px;background:var(--orange);color:var(--white);font-size:14px;display:flex;align-items:center;justify-content:center}
.field{background:var(--white);border:1px solid #d2d2d2;border-radius:2px;font-size:8px;color:#999;padding:0 8px;display:flex;align-items:center}
.field.tall{align-items:flex-start;padding-top:9px}
.book-btn{left:635px;top:14px;width:118px;height:64px;background:var(--blue);color:var(--white);font-size:10.5px;display:flex;align-items:center;justify-content:center}

/* features */
.feature{top:455px;width:175px;height:134px;border:1px solid var(--line);border-top:none}
.feature-top{height:101px;background:var(--navy);color:var(--white);display:flex;flex-direction:column;align-items:center;padding-top:20px;font-size:13px}
.feature-top svg{width:38px;height:34px;margin-bottom:14px}
.feature-top b{font-weight:700}
.feature-more{text-align:center;font-size:9.5px;color:#777;padding-top:10px}
.rule{left:127px;top:592px;width:766px;height:1px;background:var(--line)}
.rule-mark{left:127px;top:590px;width:33px;height:3px;background:var(--navy)}
.pager{left:857px;top:572px;display:flex;gap:12px}

/* news */
.section-title{left:127px;top:612px;font-size:13.5px;color:#333}
.news-rule{left:127px;top:637px;width:766px;height:1px;background:var(--line)}
.news{top:652px;width:175px}
.news-img{width:175px;height:115px}
.news-date{font-size:7px;color:#999;margin-top:7px;display:flex;align-items:center;gap:4px}
.news-title{font-size:10.5px;font-weight:700;line-height:15px;margin-top:13px;color:#222}
.news-bar{width:33px;height:2px;background:var(--navy);margin-top:4px}
.news-text{font-size:9px;color:#888;line-height:14px;margin-top:9px}
.btn{background:var(--navy);color:var(--white);font-size:9.5px;display:inline-flex;align-items:center;justify-content:center}
.news .btn{width:73px;height:23px;margin-top:8px}

/* footer */
.footer{left:0;top:912px;width:1020px;height:230px;background:var(--foot);border-top:1px solid #e6e6e6}
.col-title{top:931px;width:175px;font-size:12px;color:var(--navy);text-transform:uppercase;padding-bottom:5px;border-bottom:1px dashed #ccc}
.col-text{font-size:9px;color:#777;line-height:14px}
.about-brand{left:127px;top:1010px;display:flex;align-items:center;gap:8px;font-size:17px;font-weight:600;color:var(--navy)}
.about-brand .brand-dot{width:18px;height:18px}
.post{font-size:9px;color:#555;line-height:14px;width:175px}
.post-bar{width:33px;height:2px;background:var(--navy);margin:5px 0 10px}
.contact-line{display:flex;align-items:center;gap:8px;font-size:9px;color:#444;margin-bottom:7px}
.contact-line svg{width:11px;height:11px}
.socials{display:flex;gap:7px}
.social{width:21px;height:21px;border-radius:3px;background:var(--navy)}

.bottom{left:0;top:1142px;width:1020px;height:58px;background:var(--navy)}
.copyright{left:127px;top:1166px;font-size:8px;color:#dfe6ef}
.top-btn{left:861px;top:1155px;width:32px;height:32px;border-radius:50%;background:#111;display:flex;align-items:center;justify-content:center}
</style>
</head>
<body>

<header>
  <div class="abs brand"><span class="brand-dot"></span>Mr Colin Dwyer</div>
  <nav class="abs nav">
    <div class="nav-item active">Home<svg viewBox="0 0 7 5"><path d="M.5 .5 3.5 4 6.5 .5" fill="none" stroke="currentColor"/></svg></div>
    <div class="nav-item">Features<svg viewBox="0 0 7 5"><path d="M.5 .5 3.5 4 6.5 .5" fill="none" stroke="currentColor"/></svg></div>
    <div class="nav-item">Shortcodes<svg viewBox="0 0 7 5"><path d="M.5 .5 3.5 4 6.5 .5" fill="none" stroke="currentColor"/></svg></div>
    <div class="nav-item">Add-ons<svg viewBox="0 0 7 5"><path d="M.5 .5 3.5 4 6.5 .5" fill="none" stroke="currentColor"/></svg></div>
    <div class="nav-item">Portfolio<svg viewBox="0 0 7 5"><path d="M.5 .5 3.5 4 6.5 .5" fill="none" stroke="currentColor"/></svg></div>
    <div class="nav-item">Blog<svg viewBox="0 0 7 5"><path d="M.5 .5 3.5 4 6.5 .5" fill="none" stroke="currentColor"/></svg></div>
    <div class="nav-item">Contact</div>
  </nav>
</header>

<section>
  <div class="abs hero" role="img" aria-label="Photo of surgeons in scrubs and caps in a bright operating theatre"></div>
  <div class="abs tag">MEDICINE DEFINITION</div>
  <div class="abs headline">APPLIED SCIENCE OR PRACTICE OF THE DIAGNOSIS, TREATMENT, AND PREVENTION OF DISEASE</div>
  <div class="abs built">BUILT ON SCAFFOLD 4</div>

  <form class="abs booking">
    <div class="abs book-label">Make an Appoinment</div>
    <div class="abs field" style="left:204px;top:15px;width:131px;height:24px">Full Name</div>
    <div class="abs field" style="left:348px;top:15px;width:131px;height:24px">E-mail Address</div>
    <div class="abs field" style="left:204px;top:52px;width:131px;height:25px">Phone Number</div>
    <div class="abs field" style="left:348px;top:52px;width:131px;height:25px;justify-content:space-between">Appointment Date
      <svg width="9" height="9" viewBox="0 0 9 9"><rect x=".5" y="1.5" width="8" height="7" fill="none" stroke="#888"/><path d="M.5 3.5h8M2.5 0v2M6.5 0v2" stroke="#888"/></svg></div>
    <div class="abs field tall" style="left:491px;top:15px;width:132px;height:63px">Message</div>
    <div class="abs book-btn">Make Appointment</div>
  </form>
</section>

<section>
  <div class="abs feature" style="left:127px">
    <div class="feature-top">
      <svg viewBox="0 0 38 34" fill="#fff"><rect x="14" y="1" width="10" height="8"/><rect x="1" y="24" width="10" height="9"/><rect x="14" y="24" width="10" height="9"/><rect x="27" y="24" width="10" height="9"/><path d="M18 9h2v6h13v9h-2v-7H20v7h-2v-7H7v7H5v-9h13z"/></svg>
      <span>Exceptional <b>Service</b></span>
    </div>
    <div class="feature-more">Learn more</div>
  </div>
  <div class="abs feature" style="left:324px">
    <div class="feature-top">
      <svg viewBox="0 0 38 34" fill="none" stroke="#fff" stroke-width="2"><path d="M19 2a9 9 0 0 0-5 16.5V23h10v-4.5A9 9 0 0 0 19 2z"/><path d="M15 26h8M16 29h6M17 32h4"/><path d="M17 20v-6l2 2 2-2v6"/></svg>
      <span>Amazing <b>Design</b></span>
    </div>
    <div class="feature-more">Learn more</div>
  </div>
  <div class="abs feature" style="left:521px">
    <div class="feature-top">
      <svg viewBox="0 0 38 34" fill="none" stroke="#fff" stroke-width="2"><rect x="7" y="6" width="24" height="16" rx="1"/><path d="M2 26h34l-2 3H4z"/></svg>
      <span>Fully <b>Responsive</b></span>
    </div>
    <div class="feature-more">Learn more</div>
  </div>
  <div class="abs feature" style="left:718px">
    <div class="feature-top">
      <svg viewBox="0 0 38 34" fill="#fff"><circle cx="13" cy="19" r="9"/><circle cx="28" cy="9" r="6"/><circle cx="29" cy="26" r="5"/><g fill="#1a4a7e"><circle cx="13" cy="19" r="3.5"/><circle cx="28" cy="9" r="2.3"/><circle cx="29" cy="26" r="2"/></g><g stroke="#fff" stroke-width="3"><path d="M13 8v22M2 19h22M5 11l16 16M21 11 5 27"/></g><circle cx="13" cy="19" r="3.5" fill="#1a4a7e"/></svg>
      <span>Easy <b>Customization</b></span>
    </div>
    <div class="feature-more">Learn more</div>
  </div>
  <div class="abs rule"></div>
  <div class="abs rule-mark"></div>
  <div class="abs pager">
    <svg width="7" height="12" viewBox="0 0 7 12"><path d="M6 1 1 6l5 5" fill="none" stroke="#999" stroke-width="1.3"/></svg>
    <svg width="7" height="12" viewBox="0 0 7 12"><path d="m1 1 5 5-5 5" fill="none" stroke="#999" stroke-width="1.3"/></svg>
  </div>
</section>

<section>
  <h2 class="abs section-title" style="font-weight:400">Latest News</h2>
  <div class="abs news-rule"></div>

  <article class="abs news" style="left:127px">
    <div class="news-img" role="img" aria-label="Photo of two smiling doctors with stethoscopes" style="background:linear-gradient(135deg,#e8eef2,#b9cbd8 60%,#6e8aa3)"></div>
    <div class="news-date"><svg width="6" height="6" viewBox="0 0 6 6"><circle cx="3" cy="3" r="2.5" fill="none" stroke="#999"/></svg>Apr 22, 2013</div>
    <h3 class="news-title">Will 2013 be the year of the smartwatch?</h3>
    <div class="news-bar"></div>
    <p class="news-text">Lorem quis bibendum auctor, nisi elit consequat ipsum, nec</p>
    <span class="btn">Read More</span>
  </article>
  <article class="abs news" style="left:324px">
    <div class="news-img" role="img" aria-label="Photo of a scientist examining a flask in a laboratory" style="background:linear-gradient(135deg,#cfe6f2,#8fbfd8 55%,#4d8fb4)"></div>
    <div class="news-date"><svg width="6" height="6" viewBox="0 0 6 6"><circle cx="3" cy="3" r="2.5" fill="none" stroke="#999"/></svg>Apr 22, 2013</div>
    <h3 class="news-title">Will 2013 be the year of the smartwatch?</h3>
    <div class="news-bar"></div>
    <p class="news-text">Lorem quis bibendum auctor, nisi elit consequat ipsum, nec</p>
    <span class="btn">Read More</span>
  </article>
  <article class="abs news" style="left:521px">
    <div class="news-img" role="img" aria-label="Photo of a doctor examining a young child" style="background:linear-gradient(135deg,#d9c8c0,#c9d7e6 50%,#7d9cc0)"></div>
    <div class="news-date"><svg width="6" height="6" viewBox="0 0 6 6"><circle cx="3" cy="3" r="2.5" fill="none" stroke="#999"/></svg>Apr 22, 2013</div>
    <h3 class="news-title">Will 2013 be the year of the smartwatch?</h3>
    <div class="news-bar"></div>
    <p class="news-text">Lorem quis bibendum auctor, nisi elit consequat ipsum, nec</p>
    <span class="btn">Read More</span>
  </article>
  <article class="abs news" style="left:718px">
    <div class="news-img" role="img" aria-label="Photo of a senior doctor with an elderly patient at a laptop" style="background:linear-gradient(135deg,#e4e2de,#c8ccd0 55%,#8e98a2)"></div>
    <div class="news-date"><svg width="6" height="6" viewBox="0 0 6 6"><circle cx="3" cy="3" r="2.5" fill="none" stroke="#999"/></svg>Apr 22, 2013</div>
    <h3 class="news-title">Will 2013 be the year of the smartwatch?</h3>
    <div class="news-bar"></div>
    <p class="news-text">Lorem quis bibendum auctor, nisi elit consequat ipsum, nec</p>
    <span class="btn">Read More</span>
  </article>
</section>

<footer>
  <div class="abs footer"></div>

  <h4 class="abs col-title" style="left:127px;font-weight:400">About Us</h4>
  <div class="abs about-brand"><span class="brand-dot"></span>Mr Colin Dwyer</div>
  <p class="abs col-text" style="left:127px;top:1089px;width:180px">Curativ Theme Bibendum auctor, nisi elit consequat ipsum, nec sagittis sem nibh id elit. Duis sed odio sit amet nibh vulputate</p>

  <h4 class="abs col-title" style="left:324px;font-weight:400">Latest Posts</h4>
  <div class="abs" style="left:324px;top:966px">
    <p class="post">Update: SiteForge Theme Submission Requirements</p><div class="post-bar"></div>
    <p class="post">Marketlane's Most Wanted - $5,000 Reward for the First 15 Hosting Templates</p><div class="post-bar"></div>
    <p class="post">Does a well designed thumbnail increase your sales?</p><div class="post-bar"></div>
  </div>

  <h4 class="abs col-title" style="left:521px;font-weight:400">Contact Info</h4>
  <div class="abs" style="left:521px;top:966px;width:178px">
    <p class="col-text" style="margin-bottom:8px">Curativ Bibendum auctor, nisi elit consequat ipsum, nec sagittis sem nibh id</p>
    <div class="contact-line"><svg viewBox="0 0 11 11"><path d="M5.5 1 0 6h1.5v4h3V7h2v3h3V6H11z" fill="#333"/></svg>lorem ipsum street</div>
    <div class="contact-line"><svg viewBox="0 0 11 11"><path d="M2 1l2 2.5-1 1.2a7 7 0 0 0 3.3 3.3l1.2-1L10 9l-1.2 1.5C4.5 10 1 6.5.5 2.2z" fill="#333"/></svg>+399 (500) 264 7180</div>
    <div class="contact-line"><svg viewBox="0 0 11 11"><rect x=".5" y="2" width="10" height="7" fill="#333"/><path d="M.5 2 5.5 6l5-4" fill="none" stroke="#fff"/></svg>info@Curativ.com</div>
    <div class="socials" style="margin-top:12px"><span class="social"></span><span class="social"></span><span class="social"></span></div>
  </div>

  <h4 class="abs col-title" style="left:718px;font-weight:400">Quick Contact</h4>
  <form>
    <div class="abs field" style="left:718px;top:967px;width:87px;height:21px">Name</div>
    <div class="abs field" style="left:812px;top:967px;width:81px;height:21px">E-mail</div>
    <div class="abs field tall" style="left:718px;top:996px;width:175px;height:53px;padding-top:6px">Message</div>
    <span class="abs btn" style="left:845px;top:1058px;width:48px;height:22px">Send</span>
  </form>

  <div class="abs bottom"></div>
  <p class="abs copyright">© 2013 Curativ Theme, All Rights Reserved.</p>
  <div class="abs top-btn"><svg width="12" height="8" viewBox="0 0 12 8"><path d="M1 7l5-5 5 5" fill="none" stroke="#fff" stroke-width="1.6"/></svg></div>
</footer>

</body>
</html>
```